Restricted Contest for Business Cards and Stationery
Restricted Contest for Business Cards and Stationery - Aviation
Use same font as used in my logo
Norman T. Whitby
President
40735 Cedar Hollow Lane Tampa, Florida 33418 U.S.A.
ntwhitby@corvanetrainers.com
www.corvanetrainers.com
Please create layouts for business cards, stationary and CD labels. Keep it clean and simple. I have uploaded two files. The file including the Peregrine Falcon Head, Wing and Lettering is our logo. Please consider using the second file, just the Peregrine Head, as a "water mark" for the letterhead. Please use a simple white background. Thank you.

```html
<!DOCTYPE html>
<html lang="en">
<head>
<meta charset="utf-8">
<title>Corvane Trainers — Stationery</title>
<link href="https://fonts.googleapis.com/css2?family=Arimo:wght@400;700&display=swap" rel="stylesheet">
<style>
  :root{
    --navy:#1d2a4d;
    --navy-deep:#141e3a;
    --gold:#d7a222;
    --gold-light:#f0c75a;
    --paper:#ffffff;
    --board:#e8e9ec;
    --ink:#2b2f3a;
    --muted:#7b8090;
  }
  *{box-sizing:border-box;margin:0;padding:0}
  html,body{width:1200px;height:758px;overflow:hidden}
  body{background:var(--board);font-family:"Arimo",Arial,sans-serif;color:var(--ink);position:relative}

  .brand{display:flex;align-items:center;gap:10px;font-weight:700;color:var(--navy);letter-spacing:.08em;text-transform:uppercase;white-space:nowrap}
  .brand .dot{border-radius:50%;background:var(--gold);flex:none}

  .hero-brand{position:absolute;left:40px;top:62px;font-size:32px;gap:16px}
  .hero-brand .dot{width:52px;height:52px}

  /* Envelope */
  .envelope{position:absolute;left:228px;top:336px;width:408px;height:252px;background:var(--paper);box-shadow:0 2px 6px rgba(0,0,0,.18);overflow:hidden}
  .envelope .flap{position:absolute;left:0;top:0;width:100%;height:80px}
  .envelope .flap-brand{position:absolute;left:164px;top:12px;font-size:9px;color:#fff;gap:5px}
  .envelope .flap-brand .dot{width:12px;height:12px}
  .envelope .return-brand{position:absolute;left:16px;top:94px;font-size:13px;gap:7px}
  .envelope .return-brand .dot{width:20px;height:20px}
  .envelope .window{position:absolute;left:22px;top:152px;width:128px;height:58px;border:1px solid #9aa0ad;border-radius:4px}
  .envelope .web{position:absolute;left:200px;top:124px;font-size:9px;color:var(--navy)}
  .envelope .footer{position:absolute;left:0;bottom:0;width:100%;height:16px;background:var(--navy);border-top:2px solid var(--gold);display:flex;justify-content:space-between;align-items:center;padding:0 12px;font-size:5.5px;color:#fff}

  /* Letterhead */
  .letterhead{position:absolute;left:660px;top:12px;width:336px;height:576px;background:var(--paper);box-shadow:0 2px 6px rgba(0,0,0,.18)}
  .letterhead .head-brand{position:absolute;left:170px;top:34px;font-size:13px;gap:7px}
  .letterhead .head-brand .dot{width:22px;height:22px}
  .letterhead .body{position:absolute;left:28px;top:108px;width:280px;font-size:5.6px;line-height:1.55;color:#444}
  .letterhead .body p{margin-bottom:8px}
  .letterhead .signature{width:70px;height:16px;background:linear-gradient(90deg,#c9ccd4,#e3e5ea);margin:4px 0 4px}
  .letterhead .footer{position:absolute;left:0;bottom:0;width:100%;height:34px;background:var(--navy);border-top:3px solid var(--gold);display:flex;justify-content:space-between;align-items:center;padding:0 22px;font-size:5.6px;line-height:1.5;color:#fff}

  /* Cards */
  .card{position:absolute;top:619px;width:252px;height:125px;background:var(--paper);box-shadow:0 2px 5px rgba(0,0,0,.18);overflow:hidden}
  .card .card-brand{position:absolute;left:14px;top:14px;font-size:10.5px;gap:6px}
  .card .card-brand .dot{width:16px;height:16px}
  .card .person{position:absolute;right:16px;top:48px;text-align:right}
  .card .name{font-size:7.5px;font-weight:700;color:var(--navy)}
  .card .title{font-size:6px;color:var(--gold)}
  .card .contact{position:absolute;left:14px;top:58px;font-size:5.5px;line-height:1.5;color:#555}
  .card .band{position:absolute;left:0;bottom:0;width:100%;height:24px;display:block}
  .card .web{position:absolute;left:14px;bottom:3px;font-size:5.5px;line-height:8px;color:#fff}
  .card.right-info .person{left:14px;right:auto;text-align:left;top:46px}
  .card.right-info .contact{left:auto;right:16px;top:46px;text-align:right}
  .card.right-info .card-brand{left:auto;right:14px}
</style>
</head>
<body>

  <div class="brand hero-brand"><span class="dot"></span>Corvane Trainers</div>

  <!-- Envelope -->
  <section class="envelope">
    <svg class="flap" viewBox="0 0 408 80" preserveAspectRatio="none">
      <path d="M0 0H408V18L204 78L0 18Z" fill="var(--navy)"/>
    </svg>
    <div class="brand flap-brand"><span class="dot"></span>Corvane</div>
    <div class="brand return-brand"><span class="dot"></span>Corvane Trainers</div>
    <div class="web">www.corvanetrainers.com</div>
    <div class="window"></div>
    <div class="footer">
      <span>40735 Cedar Hollow Lane · Tampa, Florida 33418 U.S.A.</span>
      <span>+1 (813) 555-0142 · ntwhitby@corvanetrainers.com</span>
    </div>
  </section>

  <!-- Letterhead -->
  <section class="letterhead">
    <div class="brand head-brand"><span class="dot"></span>Corvane Trainers</div>
    <div class="body">
      <p>20 Mar, 2013</p>
      <p><strong>Dear Mr. Alan Porter</strong></p>
      <p>Thank you for your interest in our flight training systems. This letter outlines the simulator package we discussed, including cockpit hardware, visual display, instructor station and on-site support for your crew training program next season.</p>
      <p>Each unit is built and tested at our Tampa facility before delivery. Our engineers will stay with your team during setup and the first week of use to make sure every system runs as expected.</p>
      <p>Please review the attached schedule and pricing. We would be glad to arrange a visit so your pilots can try the trainer in person before you decide.</p>
      <p>Thank you again for your time. We look forward to working with you.</p>
      <p>Yours Sincerely,</p>
      <div class="signature" role="img" aria-label="Handwritten signature"></div>
      <p>Norman T. Whitby, President</p>
    </div>
    <div class="footer">
      <span>+1 (813) 555-0142<br>ntwhitby@corvanetrainers.com</span>
      <span>40735 Cedar Hollow Lane<br>Tampa, Florida 33418 U.S.A.</span>
    </div>
  </section>

  <!-- Business cards -->
  <article class="card" style="left:60px">
    <div class="brand card-brand"><span class="dot"></span>Corvane Trainers</div>
    <div class="person"><div class="name">Norman T. Whitby</div><div class="title">President</div></div>
    <div class="contact">40735 Cedar Hollow Lane<br>Tampa, Florida 33418 U.S.A.</div>
    <svg class="band" viewBox="0 0 252 24" preserveAspectRatio="none">
      <path d="M0 8Q126 2 252 8V24H0Z" fill="var(--navy)"/>
      <path d="M0 8Q126 2 252 8" stroke="var(--gold)" stroke-width="1.5" fill="none"/>
    </svg>
    <div class="web">www.corvanetrainers.com</div>
  </article>

  <article class="card right-info" style="left:336px">
    <div class="brand card-brand"><span class="dot"></span>Corvane Trainers</div>
    <div class="person"><div class="name">Norman T. Whitby</div><div class="title">President</div></div>
    <div class="contact">40735 Cedar Hollow Lane<br>Tampa, Florida 33418 U.S.A.<br>+1 (813) 555-0142<br>ntwhitby@corvanetrainers.com</div>
    <svg class="band" viewBox="0 0 252 24" preserveAspectRatio="none">
      <path d="M0 10Q140 4 252 5V24H0Z" fill="var(--navy)"/>
      <path d="M0 10Q140 4 252 5" stroke="var(--gold)" stroke-width="1.5" fill="none"/>
    </svg>
    <div class="web">www.corvanetrainers.com</div>
  </article>

  <article class="card" style="left:612px">
    <div class="brand card-brand"><span class="dot"></span>Corvane Trainers</div>
    <div class="person" style="top:34px"><div class="name">Norman T. Whitby</div><div class="title">President</div></div>
    <div class="contact">40735 Cedar Hollow Lane<br>Tampa, Florida 33418 U.S.A.<br>+1 (813) 555-0142<br>ntwhitby@corvanetrainers.com</div>
    <svg class="band" viewBox="0 0 252 24" preserveAspectRatio="none">
      <path d="M0 8Q126 12 252 5V24H0Z" fill="var(--navy)"/>
      <path d="M0 8Q126 12 252 5" stroke="var(--gold)" stroke-width="1.5" fill="none"/>
    </svg>
    <div class="web">www.corvanetrainers.com</div>
  </article>

  <article class="card" style="left:888px">
    <div class="brand card-brand"><span class="dot"></span>Corvane Trainers</div>
    <div class="person" style="top:34px"><div class="name">Norman T. Whitby</div><div class="title">President</div></div>
    <div class="contact">40735 Cedar Hollow Lane<br>Tampa, Florida 33418 U.S.A.<br>+1 (813) 555-0187<br>ntwhitby@corvanetrainers.com</div>
    <svg class="band" viewBox="0 0 252 24" preserveAspectRatio="none">
      <path d="M0 10H150Q200 10 252 3V24H0Z" fill="var(--navy)"/>
      <path d="M150 10Q200 10 252 3" stroke="var(--gold)" stroke-width="2" fill="none"/>
    </svg>
    <div class="web">www.corvanetrainers.com</div>
  </article>

</body>
</html>
```